5 facebook (and instagram) posts for advertising a service of Online Medicine.
This is NOT a facebook page design. This is just facebook (and Instagram) posts design.

We are a medical company providing medicine at distance, using standard videoconsultation and sometimes videoconsultation with a medical device that collects vital signs.

Each post should have:
- Our logo (attached) – if needed it can be just the circular form, but that´s up to you to decide. Ofcourse some design work can be done to this form (watermark, change in dimension, etc)
- Some posts can have the photo of the device (not all the posts because we also provide videoconsultations without the device) – for this please use our website to collect images (https://www.casaorvalhoverde.com/en/kordalix). You can also use the video of the device to collect images (provided as attachment).
- Some stock image at your decision or collected from our website (https://www.casaorvalhoverde.com/pt/medicina-online) or from the provided video (all of these are licensed and you can use them freely – for instance you can collect doctors from our video)
- One or more of the following headlines (please use different headlines for different posts):
 Revolução na Qualidade da Videoconsulta
 O seu Médico com acesso à informação da sua Orrin Wellbook
 Sincronização com Orrin Wellbook
 Possibilidade de usar o dispositivo Kordalix | Medição à Distância de 6 Sinais Vitais
 Revolução na Saúde
 Revolução na Medicina à Distância
 Um Novo Mundo na Saúde
 Segurança e Fiabilidade na Medicina à Distância
 Excelência na Medicina à Distância
 Baixa Médica Online
 Atestados de Saúde
 Renovação de Receituário
 Planos de Monitorização Remota e Acompanhamento Médico desde 10 EUR / Mês

We need 5 posts, all different between each other but where we can feel an aesthetical and graphic/design continuity/coherence of course.
Each post should be provided on adequate format for facebook and Instagram publishing.

Target Market(s)

Patients

Industry/Entity Type

Medicine

Requirements
Must have
• Check description
Nice to have
• Check description

```html
<!DOCTYPE html>
<html lang="pt">
<head>
<meta charset="utf-8">
<title>Casa Orvalho Verde — Posts</title>
<link href="https://fonts.googleapis.com/css2?family=Barlow+Semi+Condensed:wght@600;700&family=Poppins:wght@400;500&display=swap" rel="stylesheet">
<style>
:root{
  --bg:#ffffff;
  --post:#deedfc;
  --blue:#1ea4d9;
  --blue-deep:#1683b5;
  --ink:#0c1a28;
  --chip:#eef6fe;
  --photo-a:#b9d3ea;
  --photo-b:#7fa9cc;
}
*{box-sizing:border-box;margin:0;padding:0}
html,body{width:1200px;height:801px;overflow:hidden;background:var(--bg)}
body{position:relative;font-family:"Poppins",sans-serif;color:var(--ink)}
.post{position:absolute;width:383px;height:383px;background:var(--post);overflow:hidden}
.p1{left:15px;top:12px}.p2{left:409px;top:12px}.p3{left:803px;top:12px}
.p4{left:15px;top:406px}.p5{left:409px;top:406px}.p6{left:803px;top:406px}
.abs{position:absolute}

.brand{position:absolute;display:flex;align-items:center;gap:6px;z-index:2}
.brand.center{left:50%;transform:translateX(-50%)}
.brand-dot{width:22px;height:22px;border-radius:50%;background:var(--blue);flex:none}
.brand-text{display:flex;flex-direction:column;line-height:1}
.brand-name{font-family:"Barlow Semi Condensed",sans-serif;font-weight:700;font-size:17px;color:var(--blue);text-transform:uppercase;letter-spacing:.2px;white-space:nowrap}
.brand-sub{font-size:6.5px;color:var(--blue);margin-top:2px;white-space:nowrap}

.headline{position:absolute;z-index:2;font-family:"Barlow Semi Condensed",sans-serif;font-weight:700;color:var(--ink);line-height:1.12;white-space:nowrap}
.headline.center{left:0;right:0;text-align:center}
.accent{color:var(--blue);text-decoration:underline;text-decoration-thickness:1.5px;text-underline-offset:4px}
.subline{position:absolute;z-index:2;left:0;right:0;text-align:center;font-size:12px;color:var(--ink)}

.cta{position:absolute;z-index:2;background:var(--blue);color:#fff;border-radius:20px;display:flex;align-items:center;justify-content:center;font-family:"Barlow Semi Condensed",sans-serif;font-weight:600;box-shadow:0 4px 8px rgba(30,164,217,.25)}
.url{position:absolute;z-index:2;text-align:center;font-size:11.5px;color:var(--ink)}

.chip{position:absolute;z-index:3;background:var(--chip);border-radius:10px;display:flex;align-items:center;gap:7px;padding:0 8px;font-size:6.6px;font-weight:500;line-height:1.2;box-shadow:0 2px 6px rgba(30,100,160,.08)}
.tick{width:19px;height:19px;border-radius:50%;background:#d7e9f9;display:flex;align-items:center;justify-content:center;flex:none}

.photo{position:absolute;background:linear-gradient(160deg,var(--photo-a),var(--photo-b))}
.figure{position:absolute;z-index:1}
.ring{position:absolute;border:1.2px dashed var(--blue);border-radius:50%;opacity:.7}
.icon-dot{position:absolute;z-index:2;width:16px;height:16px;border-radius:50%;background:var(--blue);border:2px solid #fff}

.bullets{position:absolute;z-index:2;list-style:none;font-size:9px;line-height:1.38;white-space:nowrap}
.bullets li{display:flex;align-items:center;gap:4px}
.bullets li::before{content:"";width:5px;height:5px;border-radius:50%;background:var(--blue)}
</style>
</head>
<body>

<svg width="0" height="0" style="position:absolute">
  <defs>
    <linearGradient id="photoTone" x1="0" y1="0" x2="0.6" y2="1">
      <stop offset="0" stop-color="#b9d3ea"/><stop offset="1" stop-color="#7fa9cc"/>
    </linearGradient>
  </defs>
  <symbol id="check" viewBox="0 0 12 12"><path d="M6 1 L10 2.5 V6 C10 8.5 8 10.2 6 11 C4 10.2 2 8.5 2 6 V2.5 Z" fill="#1ea4d9"/><path d="M4.2 6 L5.6 7.3 L8 4.8" stroke="#fff" stroke-width="1.1" fill="none"/></symbol>
</svg>

<!-- Post 1 -->
<section class="post p1">
  <div class="brand center" style="top:14px">
    <span class="brand-dot"></span>
    <span class="brand-text"><span class="brand-name">Casa Orvalho Verde</span><span class="brand-sub">Professor Doutor Tiago Ferrel</span></span>
  </div>
  <h2 class="headline center" style="top:80px;font-size:29px">Consulte seus <span class="accent">médicos</span></h2>
  <p class="subline" style="top:112px">através de videoconsulta</p>
  <div class="ring" style="left:92px;top:153px;width:212px;height:212px"></div>
  <div class="photo" role="img" aria-label="Médica sorridente de farda azul" style="left:95px;top:195px;width:90px;height:100px;transform:rotate(-14deg);border-radius:8px"></div>
  <div class="photo" role="img" aria-label="Jovem médica sorridente" style="left:154px;top:175px;width:84px;height:92px;border-radius:8px"></div>
  <div class="photo" role="img" aria-label="Médico sorridente com estetoscópio" style="left:215px;top:195px;width:95px;height:100px;transform:rotate(16deg);border-radius:8px"></div>
  <span class="icon-dot" style="left:253px;top:162px"></span>
  <span class="icon-dot" style="left:84px;top:250px"></span>
  <span class="icon-dot" style="left:293px;top:264px"></span>
  <div class="chip" style="left:42px;top:156px;width:94px;height:42px"><span class="tick"><svg width="12" height="12"><use href="#check"/></svg></span>Consulta de Rotina ou Urgência</div>
  <div class="cta" style="left:94px;top:309px;width:196px;height:36px;font-size:16px">Marque a sua consulta</div>
  <p class="url" style="left:0;right:0;top:348px">casaorvalhoverde.com</p>
</section>

<!-- Post 2 -->
<section class="post p2">
  <div class="brand" style="left:13px;top:26px">
    <span class="brand-dot"></span>
    <span class="brand-text"><span class="brand-name">Casa Orvalho Verde</span><span class="brand-sub">Professor Doutor Tiago Ferrel</span></span>
  </div>
  <div class="abs" style="left:178px;top:220px;width:260px;height:260px;border-radius:50%;background:var(--blue)"></div>
  <svg class="figure" role="img" aria-label="Médico sorridente de bata branca com estetoscópio e prancheta" style="left:200px;top:72px" width="183" height="311" viewBox="0 0 183 311">
    <path d="M64 50 Q64 0 117 0 Q170 0 170 50 L170 82 Q183 92 183 104 L183 311 L6 311 L6 150 Q6 100 64 90 Z" fill="url(#photoTone)"/>
  </svg>
  <h2 class="headline" style="left:14px;top:102px;font-size:26px">Marque a sua consulta<br>médica <span class="accent">remota</span></h2>
  <ul class="bullets" style="left:15px;top:188px">
    <li>O seu médico com o clique de um botão</li>
    <li>Qualquer dia, a qualquer hora</li>
    <li>Monitorização remota de pacientes</li>
    <li>Controlo rigoroso da sua doença crónica</li>
    <li>Qualidade e segurança</li>
    <li>Serviço sem fronteiras</li>
    <li>Consultas gerais e de especialidade</li>
  </ul>
  <div class="cta" style="left:22px;top:301px;width:144px;height:24px;font-size:11.5px">Marque a sua consulta</div>
  <p class="url" style="left:22px;width:144px;top:330px;font-size:9px">casaorvalhoverde.com</p>
  <div class="chip" style="left:255px;top:316px;width:94px;height:40px"><span class="tick"><svg width="12" height="12"><use href="#check"/></svg></span>Consulta de Rotina ou Urgência</div>
</section>

<!-- Post 3 -->
<section class="post p3">
  <div class="brand" style="left:13px;top:26px">
    <span class="brand-dot"></span>
    <span class="brand-text"><span class="brand-name">Casa Orvalho Verde</span><span class="brand-sub">Professor Doutor Tiago Ferrel</span></span>
  </div>
  <div class="abs" style="left:250px;top:240px;width:200px;height:200px;border-radius:50%;background:var(--blue)"></div>
  <div class="ring" style="left:160px;top:95px;width:220px;height:220px"></div>
  <span class="icon-dot" style="left:186px;top:112px"></span>
  <span class="icon-dot" style="left:320px;top:106px"></span>
  <span class="icon-dot" style="left:170px;top:196px"></span>
  <svg class="figure" role="img" aria-label="Médico sorridente de bata branca com estetoscópio e prancheta" style="left:172px;top:72px" width="211" height="311" viewBox="0 0 211 311">
    <path d="M66 50 Q66 0 112 0 Q158 0 158 50 L158 85 Q211 95 211 140 L211 311 L0 311 L0 140 Q0 95 66 85 Z" fill="url(#photoTone)"/>
  </svg>
  <h2 class="headline" style="left:14px;top:76px;font-size:26px;line-height:1.22">O seu médico em<br><span class="accent">movimento</span></h2>
  <div class="photo" role="img" aria-label="Ecrã de aplicação de marcação de consulta com horários disponíveis" style="left:28px;top:160px;width:140px;height:240px;border-radius:18px;transform:rotate(-10deg);background:linear-gradient(170deg,#ffffff,#e8f2fb);box-shadow:0 6px 16px rgba(20,80,140,.15);z-index:2"></div>
  <div class="chip" style="left:256px;top:316px;width:94px;height:40px"><span class="tick"><svg width="12" height="12"><use href="#check"/></svg></span>Consulta de Rotina ou Urgência</div>
</section>

<!-- Post 4 -->
<section class="post p4">
  <div class="brand center" style="top:14px">
    <span class="brand-dot"></span>
    <span class="brand-text"><span class="brand-name">Casa Orvalho Verde</span><span class="brand-sub">Professor Doutor Tiago Ferrel</span></span>
  </div>
  <h2 class="headline center" style="top:60px;font-size:24px;line-height:1.2">Revolução na<br>Medicina à <span class="accent">distância</span></h2>
  <p class="subline" style="top:117px">Consulta de rotina ou Urgência</p>
  <div class="photo" role="img" aria-label="Telemóvel com médico sorridente de farda azul na aplicação" style="left:70px;top:165px;width:148px;height:230px;border-radius:20px"></div>
  <div class="photo" role="img" aria-label="Telemóvel com ecrã de dados de saúde do paciente" style="left:180px;top:218px;width:140px;height:180px;border-radius:18px;background:linear-gradient(180deg,var(--blue-deep) 0 18%,#f7fbff 18%);box-shadow:0 6px 16px rgba(20,80,140,.15)"></div>
  <div class="chip" style="left:265px;top:168px;width:86px;height:36px;font-size:6.5px"><span style="width:15px;height:15px;border-radius:50%;background:#f5c43a;flex:none"></span>Pacientes felizes</div>
  <div class="chip" style="left:25px;top:312px;width:94px;height:40px"><span class="tick"><svg width="12" height="12"><use href="#check"/></svg></span>Consulta de Rotina ou Urgência</div>
</section>

<!-- Post 5 -->
<section class="post p5">
  <div class="brand center" style="top:14px">
    <span class="brand-dot"></span>
    <span class="brand-text"><span class="brand-name">Casa Orvalho Verde</span><span class="brand-sub">Professor Doutor Tiago Ferrel</span></span>
  </div>
  <h2 class="headline center" style="top:59px;font-size:24px;line-height:1.2">Acompanhamento<br>médico com <span class="accent">Kordalix</span></h2>
  <p class="subline" style="top:118px">Medição Remota de 6 Sinais Vitais</p>
  <div class="ring" style="left:90px;top:152px;width:210px;height:210px"></div>
  <span class="icon-dot" style="left:246px;top:160px"></span>
  <span class="icon-dot" style="left:83px;top:250px"></span>
  <span class="icon-dot" style="left:287px;top:260px"></span>
  <div class="photo" role="img" aria-label="Dispositivo Kordalix de medição de sinais vitais com ecrã tátil" style="left:105px;top:175px;width:182px;height:115px;border-radius:40px;background:linear-gradient(160deg,#3a3f45,#111)"></div>
  <div class="chip" style="left:42px;top:157px;width:94px;height:42px"><span class="tick"><svg width="12" height="12"><use href="#check"/></svg></span>Consulta de Rotina ou Urgência</div>
  <div class="cta" style="left:81px;top:307px;width:222px;height:34px;font-size:15px">Desde 10 EUR/mês</div>
  <p class="url" style="left:0;right:0;top:349px">casaorvalhoverde.com</p>
</section>

<!-- Post 6 -->
<section class="post p6">
  <div class="brand center" style="top:14px">
    <span class="brand-dot"></span>
    <span class="brand-text"><span class="brand-name">Casa Orvalho Verde</span><span class="brand-sub">Professor Doutor Tiago Ferrel</span></span>
  </div>
  <div class="abs" style="left:150px;top:132px;width:210px;height:210px;border-radius:50%;background:var(--blue)"></div>
  <div class="photo" role="img" aria-label="Médico sénior de bata branca com braços cruzados" style="left:160px;top:86px;width:190px;height:256px;border-radius:90px 90px 100px 100px"></div>
  <h2 class="headline" style="left:20px;top:64px;font-size:23px;line-height:1.22">Segurança e<br>Fiabilidade na<br>Medicina a<br><span class="accent">Distância</span></h2>
  <div class="chip" style="left:14px;top:196px;width:105px;height:40px"><span class="tick"><svg width="12" height="12"><use href="#check"/></svg></span>Consultas de Rotina e Urgência</div>
  <div class="chip" style="left:14px;top:242px;width:111px;height:40px"><span class="tick"><svg width="12" height="12"><use href="#check"/></svg></span>Acompanhamento Geral de Saúde</div>
  <div class="chip" style="left:14px;top:288px;width:121px;height:40px"><span class="tick"><svg width="12" height="12"><use href="#check"/></svg></span>Acompanhamento de Doença Crónica</div>
  <p class="url" style="left:150px;width:210px;top:348px">casaorvalhoverde.com</p>
</section>

</body>
</html>
```